KVR Fashion Design Company Needs a New Web Design, Please Click Me

Designers:

PLEASE NOTE: we only need the web page design, not a fully coded website.

Our brand's name is The Amber Loft, our signature is print. our style is edgy and chic.

The old website is too messy. here's the address:
www.kvrstudio-example.com.cn

The new website's purpose is to show our brand/design and most importantly, sell products, So it should be a combination of a designer official website and online shopping. I want the whole style to be clean, edgy and pioneer, easy to understand. we need a sophisticated online shopping website.

The reference websites are:
lumorivet.co.uk
www.qd-pelm.com
dariustoke.com
belusarno.com
fenwirapadlos.com

Please beat their designs :)

Check out our lasted fashion show to get to know us more.

https://www.vidstreamexample.com/watch?v=ZtrmKqLwXbPo&spfreload=10

The attachments are our Logo and some 2015 Look Book.
(Please let us know if you want to play with our print in this particular web design, we can send the source file.)
Updates

Designers, we really like the design of marisolvantree.com(we have attached a picture of the website) , Can we get a homepage like that? so the designs you submit will be 3 pages. The first one should be a page that only has Shop/Look. then the shop page, it should be nothing but our product which we will list the categories ourself. And the look page should contain all the info. such as news, about us and designers etc. Thank you all for your hard work, we really enjoyed the designs. Added Monday, November 03, 2014

Target Market(s)

Our target audiences are woman aged from 16-40 who like online shopping

Industry/Entity Type

Online Shopping

Number of Pages Required

3 page

Font styles to use
Serif
Sans Serif
Script

Requirements
Must have
• Designers,
• we really like the design of marisolvantree.com(we have attached a picture of the website) , Can we get a homepage like that? so the designs you submit will be 3 pages. The first one should be a page that only has Shop/Look. then the shop page, it should be nothing but our product which we will list the categories ourself. And the look page should contain all the info. such as news, about us and designers etc. Thank you all for your hard work, we really enjoyed the designs.

```html
<!DOCTYPE html>
<html lang="en">
<head>
<meta charset="utf-8">
<title>The Amber Loft — Home</title>
<link rel="stylesheet" href="https://fonts.googleapis.com/css2?family=Lora:wght@400&family=Raleway:wght@400;500&display=swap">
<style>
  :root {
    --ink: #1a1a1a;
    --muted: #333333;
    --accent: #b3201f;
    --rule: #cfcfcf;
    --paper: #ffffff;
  }
  * { margin: 0; padding: 0; box-sizing: border-box; }
  html, body { width: 1200px; height: 675px; overflow: hidden; background: var(--paper); }
  body { position: relative; font-family: "Raleway", Arial, sans-serif; color: var(--ink); }

  .brand { position: absolute; left: 115px; top: 18px; width: 112px; text-align: center; }
  .brand-mark { display: block; width: 40px; height: 40px; margin: 0 auto 6px; border-radius: 50%; background: var(--accent); }
  .brand-name { font-family: "Lora", Georgia, serif; font-size: 10.5px; line-height: 9.5px; letter-spacing: 0.6px; color: var(--ink); text-transform: uppercase; white-space: nowrap; }

  .main-nav { position: absolute; top: 53px; left: 669px; display: flex; align-items: center; font-size: 9.5px; }
  .main-nav a { color: var(--muted); text-decoration: none; margin-right: 23px; }
  .main-nav a.is-active { color: var(--accent); }
  .cart { position: absolute; left: 1033px; top: 52px; display: flex; align-items: center; gap: 8px; font-size: 9px; }
  .search { position: absolute; left: 1075px; top: 54px; }

  .page-title { position: absolute; left: 116px; top: 198px; font-family: "Lora", Georgia, serif; font-weight: 400; font-size: 37px; color: var(--ink); }
  .follow { position: absolute; left: 961px; top: 222px; display: flex; align-items: center; font-size: 9px; color: var(--muted); }
  .follow span { margin-right: 10px; }
  .social-dot { display: inline-block; width: 7px; height: 7px; border-radius: 50%; background: var(--ink); margin-right: 13px; }

  .rule { position: absolute; left: 117px; width: 966px; height: 1px; background: var(--rule); }
  .rule-top { top: 254px; }
  .rule-bottom { top: 505px; }

  .intro { position: absolute; left: 117px; top: 266px; width: 360px; font-size: 9px; line-height: 18px; color: var(--muted); }
  .carousel-controls { position: absolute; left: 1056px; top: 279px; display: flex; gap: 11px; }

  .lookbook { position: absolute; top: 324px; left: 117px; display: flex; gap: 15.5px; }
  .look { width: 125px; height: 156px; }
  .look-1 { border: 1px solid #d8d8d8; background: linear-gradient(180deg, #f4f0ee 0%, #c9472c 35%, #a8301f 62%, #1e1a1a 100%); }
  .look-2 { background: linear-gradient(160deg, #0d1624 0%, #3a6aa8 45%, #1f3d6e 75%, #0a0f18 100%); }
  .look-3 { background: linear-gradient(180deg, #d9d9d9 0%, #3b3e44 40%, #2c2e33 75%, #6c6c6c 100%); }
  .look-4 { background: linear-gradient(160deg, #0c1a2e 0%, #3b5f8f 35%, #c9b3a6 60%, #3d5a7e 85%, #111a28 100%); }
  .look-5 { background: linear-gradient(180deg, #e6e6e6 0%, #3a2a30 35%, #5a3a44 65%, #d9d2c8 100%); }
  .look-6 { background: linear-gradient(180deg, #f2f3f3 0%, #dfe1e1 45%, #f5f5f5 75%, #cfd2d2 100%); }
  .look-7 { background: linear-gradient(160deg, #d4ecf8 0%, #6fb6e0 40%, #1f6fb4 70%, #8ccbee 100%); }

  .shop-now { position: absolute; left: 540px; top: 534px; width: 121px; height: 34px; background: var(--accent); color: #fff; font-size: 16.5px; line-height: 34px; text-align: center; text-decoration: none; letter-spacing: 0.2px; }

  .copyright { position: absolute; right: 117px; top: 632px; font-size: 7.5px; color: var(--ink); }
</style>
</head>
<body>
  <header>
    <a class="brand" href="#">
      <span class="brand-mark"></span>
      <span class="brand-name">KVR Group<br>The Amber Loft</span>
    </a>
    <nav class="main-nav">
      <a class="is-active" href="#">Home</a>
      <a href="#">About</a>
      <a href="#">Designer</a>
      <a href="#">News</a>
      <a href="#">Members Center</a>
      <a href="#">Shop Now</a>
    </nav>
    <div class="cart">
      <svg width="11" height="13" viewBox="0 0 11 13" aria-hidden="true"><path d="M1 4h9v8H1z" fill="none" stroke="#1a1a1a" stroke-width="1.3"/><path d="M3.3 4V2.8a2.2 2.2 0 0 1 4.4 0V4" fill="none" stroke="#1a1a1a" stroke-width="1.2"/></svg>
      <span>3</span>
    </div>
    <svg class="search" width="10" height="10" viewBox="0 0 10 10" aria-label="Search"><circle cx="4" cy="4" r="3" fill="none" stroke="#1a1a1a" stroke-width="1.6"/><path d="M6.2 6.2 9.2 9.2" stroke="#1a1a1a" stroke-width="1.8"/></svg>
  </header>

  <main>
    <h1 class="page-title">The Amber Loft</h1>
    <div class="follow">
      <span>Follow us:</span>
      <i class="social-dot" aria-label="Social network 1"></i>
      <i class="social-dot" aria-label="Social network 2"></i>
      <i class="social-dot" aria-label="Social network 3"></i>
      <i class="social-dot" aria-label="Social network 4"></i>
    </div>
    <div class="rule rule-top"></div>

    <p class="intro">A hand shop to buy the product in the form of collection of designer fashion stores as well as personal customization combined boutiques.</p>
    <div class="carousel-controls">
      <svg width="6" height="9" viewBox="0 0 6 9" aria-label="Previous"><path d="M5 1 1.5 4.5 5 8" fill="none" stroke="#1a1a1a" stroke-width="1.4"/></svg>
      <svg width="6" height="9" viewBox="0 0 6 9" aria-label="Next"><path d="M1 1l3.5 3.5L1 8" fill="none" stroke="#1a1a1a" stroke-width="1.4"/></svg>
    </div>

    <div class="lookbook">
      <div class="look look-1" role="img" aria-label="Model in an orange print cut-out top with black skirt"></div>
      <div class="look look-2" role="img" aria-label="Model in a blue textured dress against a dark backdrop"></div>
      <div class="look look-3" role="img" aria-label="Man in a charcoal suit with waistcoat"></div>
      <div class="look look-4" role="img" aria-label="Model in a multicolour print dress"></div>
      <div class="look look-5" role="img" aria-label="Man in a dark patterned print shirt"></div>
      <div class="look look-6" role="img" aria-label="Model in a white cropped jacket and full skirt"></div>
      <div class="look look-7" role="img" aria-label="Model in a blue print jumpsuit"></div>
    </div>

    <div class="rule rule-bottom"></div>
    <a class="shop-now" href="#">SHOP NOW</a>
  </main>

  <footer class="copyright">Copyright @ 2014 &nbsp;The Amber Loft &nbsp;All rights reserved.</footer>
</body>
</html>
```